Clean and Polished Store Design

Please design a website similar to this one: http://velmarixa.com/
We require two pages:
* the home page: http://velmarixa.com/
* the product page: http://velmarixa.com/products/our-printer
Notice that there are few words and more pictures. It's clean and professional. Although I think their product page is difficult to read because it is too spread out.
Please help us generate excitement for our product via a polished and high-end looking web design. Please keep it VERY SIMPLE.
Target Market(s)
Our target market is consumers that have never bought a 3D printer before and those to whom 3D printing is new but exciting. Our market is not very technical. They love the sleek look of the printer and its ease of use.
Industry/Entity Type
Printer
Requirements
Must have
- We require two pages:
- * the home page: http://velmarixa.com/
- * the product page: http://velmarixa.com/products/our-printer
- One of our product renderings must be displayed on both the homepage and the product page.
- Our logo must be displayed on both pages.
- The pages must have a header, a footer and content equivalent to the velmarixa website.

```html
<!DOCTYPE html>
<html lang="en">
<head>
<meta charset="utf-8">
<title>Brintal 3D — The Vela 1 Desktop 3D Printer</title>
<link rel="stylesheet" href="https://fonts.googleapis.com/css2?family=Source+Sans+3:wght@400;700&display=swap">
<style>
  :root {
    --ink: #111111;
    --paper: #ffffff;
    --copper-dark: #8a5a45;
    --copper-mid: #c99078;
    --copper-light: #fbe0d1;
    --copper-base: #ae6c4b;
    --amber: #c9722f;
    --amber-light: #e09a52;
    --press-mark: #2a2a2a;
  }
  * { box-sizing: border-box; margin: 0; padding: 0; }
  html, body { width: 1200px; height: 1000px; overflow: hidden; background: var(--paper); }
  body { font-family: "Source Sans 3", "Myriad Pro", Arial, sans-serif; color: var(--ink); }
  .canvas { position: relative; width: 1200px; height: 1000px; }
  .abs { position: absolute; }

  .copper {
    background: linear-gradient(180deg, var(--copper-dark) 0%, var(--copper-mid) 35%, var(--copper-light) 72%, var(--copper-mid) 88%, var(--copper-base) 100%);
  }
  .copper-button {
    position: absolute;
    display: flex; align-items: center; justify-content: center;
    background: linear-gradient(180deg, var(--copper-base) 0%, var(--copper-light) 45%, var(--copper-light) 60%, var(--copper-base) 100%);
    color: var(--ink); font-size: 15px; text-decoration: none; white-space: nowrap;
  }

  .brand { left: 309px; top: 60px; display: flex; align-items: center; gap: 10px; }
  .brand-name { font-size: 44px; font-weight: 700; letter-spacing: -0.5px; line-height: 1; }
  .brand-mark { width: 26px; height: 26px; background: var(--ink); }

  .main-nav { top: 126px; left: 522px; font-size: 13.5px; }
  .main-nav a { position: absolute; top: 0; color: var(--ink); text-decoration: none; white-space: nowrap; }

  .hero { left: 309px; top: 151px; width: 584px; height: 211px; }
  .placeholder-word { position: absolute; font-size: 52px; line-height: 1; }
  .hero-lines { left: 15px; top: 116px; font-size: 13.5px; line-height: 18px; position: absolute; }

  .intro-title { left: 309px; top: 401px; font-size: 15.5px; line-height: 24px; }
  .intro-body { left: 310px; top: 461px; width: 230px; font-size: 13.5px; line-height: 21px; }

  .video { left: 569px; top: 395px; width: 324px; height: 179px; }
  .video-label { position: absolute; top: 36px; left: 0; width: 100%; text-align: center; font-size: 12.5px; }

  .press-mark { position: absolute; height: 12px; background: var(--press-mark); border-radius: 1px; }

  .updates-label { left: 309px; top: 774px; font-size: 13.5px; }

  .footer-band { left: 309px; top: 806px; width: 584px; height: 177px;
    background: linear-gradient(135deg, var(--amber) 0%, var(--amber-light) 50%, var(--amber) 100%); }
  .footer-title { position: absolute; left: 0; top: 22px; font-size: 14.5px; }
  .footer-tagline { position: absolute; left: 2px; top: 43px; font-size: 14.5px; }
  .footer-brand { position: absolute; left: 96px; top: 130px; font-size: 16px; }
  .footer-nav { position: absolute; left: 269px; top: 141px; font-size: 12.5px; white-space: nowrap; }
  .footer-nav a { color: var(--ink); text-decoration: none; margin-right: 4px; }
  .footer-legal { position: absolute; left: 286px; top: 158px; font-size: 12.5px; white-space: nowrap; }
  .product-render { position: absolute; left: 445px; top: 28px; width: 132px; height: 104px;
    background: linear-gradient(180deg, #b5611f 0%, #d9a36a 45%, #e9e9ea 70%, #f4f4f4 100%); border-radius: 6px; }
</style>
</head>
<body>
<div class="canvas">

  <header>
    <a class="brand abs" href="http://velmarixa.com/" style="text-decoration:none;color:var(--ink)">
      <span class="brand-name">Brintal 3D</span>
      <span class="brand-mark"></span>
    </a>
    <nav class="main-nav abs">
      <a href="http://velmarixa.com/products/our-printer" style="left:0">THE VELA 1</a>
      <a href="#" style="left:77px">BLOG</a>
      <a href="#" style="left:119px">SUPPORT</a>
      <a href="#" style="left:183px">ABOUT US</a>
      <a href="#" style="left:320px">0</a>
      <a href="#" style="left:337px">LOGIN</a>
    </nav>
    <a class="copper-button" href="#" style="left:772px;top:122px;width:52px;height:25px;font-size:14px">STORE</a>
  </header>

  <main>
    <section class="hero abs copper" role="img" aria-label="Hero rendering of the Vela 1 desktop 3D printer">
      <span class="placeholder-word" style="left:229px;top:80px">IMAGE</span>
      <div class="hero-lines">THE VELA 1 3D<br>HIGH RESOLUTION<br>Desktop 3D Printer</div>
    </section>
    <a class="copper-button" href="#" style="left:324px;top:331px;width:161px;height:24px">Pre-order your Vela 1 !</a>

    <h1 class="intro-title abs" style="font-weight:400">The Precision of Stereolithography.<br>Right on Your Desktop.</h1>
    <p class="intro-body abs">The Vela 1 marries high-end stereolithography ( SL ) technology and a seamless user experience at a price affordable to the professional designer, engineer and maker.</p>
    <a class="copper-button" href="http://velmarixa.com/products/our-printer" style="left:309px;top:576px;width:108px;height:24px">Learn more ›</a>

    <section class="video abs copper" role="img" aria-label="Introduction video for the Vela 1">
      <div class="video-label">INTRODUCTION VELA 1</div>
      <span class="placeholder-word" style="left:92px;top:72px">VIDEO</span>
    </section>

    <section class="press" aria-label="As featured in">
      <span class="press-mark" style="left:343px;top:646px;width:74px"></span>
      <span class="press-mark" style="left:470px;top:647px;width:74px"></span>
      <span class="press-mark" style="left:568px;top:648px;width:52px"></span>
      <span class="press-mark" style="left:677px;top:647px;width:68px"></span>
      <span class="press-mark" style="left:785px;top:650px;width:43px"></span>
      <span class="press-mark" style="left:344px;top:694px;width:68px"></span>
      <span class="press-mark" style="left:469px;top:693px;width:54px;height:15px"></span>
      <span class="press-mark" style="left:571px;top:696px;width:63px"></span>
      <span class="press-mark" style="left:677px;top:695px;width:84px"></span>
      <span class="press-mark" style="left:785px;top:696px;width:68px"></span>
    </section>

    <section class="updates">
      <div class="updates-label abs">Get Updates on Our Progress:</div>
      <a class="copper-button" href="#" style="left:569px;top:769px;width:108px;height:25px">Enter E-mail</a>
      <a class="copper-button" href="#" style="left:783px;top:769px;width:110px;height:25px">Stay in Touch</a>
    </section>
  </main>

  <footer class="footer-band abs" role="img" aria-label="Warm wood-tone patterned footer band">
    <div class="footer-title">THE VELA 1&nbsp; 3D&nbsp; PRINTER</div>
    <div class="footer-tagline">An affordable, high-resolution 3D printer for professional creators</div>
    <a class="copper-button" href="#" style="left:0;top:75px;width:161px;height:25px">Pre-order your Vela 1!</a>
    <div class="product-render" role="img" aria-label="Product rendering of the Vela 1 printer with printed sample parts"></div>
    <div class="footer-brand">velmarixa</div>
    <nav class="footer-nav">
      <a href="http://velmarixa.com/products/our-printer">THE VELA 1</a><a href="#">BLOG</a><a href="#">SUPPORT</a><a href="#">ABOUT US</a><a href="#">STORE</a><a href="#">CAREERS</a>
    </nav>
    <div class="footer-legal">© Velmarixa 2012 - Privacy Policy - Terms of Service</div>
  </footer>

</div>
</body>
</html>
```